Book Cover Design for Carry the HOPE

The title continues with shaped by Heaven's Outline to Pursue Excellence in kindness to neighbours. So HOPE is an acronym for Heaven's Outline Pursuing Excellence. I wrote the book based on what God taught me when my adult daughter passed away. I failed to recognize her gifts of helping people feel valued and loved. Through this discovery, I recognized I had an identity crisis which prevented me from using the gifts God gave me to serve others. The book chapters include: (1) Carry the HOPE, (2) The Author of the HOPE, (3) Beware the HOPE Robber, (4) Defenders of the HOPE, (5) The Purpose of the HOPE, (6) The Manifestation of the HOPE, (7) The Empowerment of the HOPE and (9) The Reward of the HOPE. Please let me know what other information would be helpful in designing my book cover
Target Market(s)
The book is intended for Christians who surrendered just enough to get saved but did not surrender enough for God to transform them to become more Christ-like.
Industry/Entity Type
Christian
Requirements
Must have
- Please ensure each letter in the word HOPE is a different color. Next, ensure the first leet of the words Heaven's Outline and Pursuing Excellence in the make in .... are the same color as the associate letter in HOPE.
For this project, I just want the front cover. I will create a separate paid project for the selected designer to complete the spine and back cover before publishing through Brindlecart.
Nice to have
- Is it possible to make the cover look like a gift you would receive
I also attached potential design ideas for layout. I want to see your creativity come out in the design.
Should not have
- Not applicable

```html
<!DOCTYPE html>
<html lang="en">
<head>
<meta charset="utf-8">
<title>Carry the HOPE – Book Cover</title>
<link rel="stylesheet" href="https://fonts.googleapis.com/css2?family=Audiowide&family=Cinzel:wght@400;600&family=Cormorant+Garamond:ital,wght@1,500;1,600&family=Montserrat:ital,wght@0,700;0,900;1,900&family=Oswald:wght@500;600&family=Playfair+Display:ital,wght@1,600&display=swap">
<style>
  :root {
    --stage: #e9e4dc;
    --back-bg: #151515;
    --back-teal: #1fb3b0;
    --back-pink: #e2357a;
    --back-rule: #a3172a;
    --back-head: #e8e8e8;
    --back-muted: #9a9a9a;
    --front-top: #fbd6c8;
    --front-mid: #f8b45a;
    --front-warm: #f39a2b;
    --hope-h: #e8238a;
    --hope-o: #7b2fd0;
    --hope-p: #f07a12;
    --hope-e: #12a6a0;
    --title-yellow: #ffe14d;
    --title-stroke: #6a2ca0;
    --subtitle-blue: #2d4fa8;
    --byline: #138f8c;
    --word-yellow: #fff1a0;
    --band-orange: #e9821d;
    --band-red: #8a1424;
    --band-black: #111111;
    --white: #ffffff;
  }
  * { box-sizing: border-box; margin: 0; padding: 0; }
  html, body { width: 1200px; height: 799px; overflow: hidden; }
  body { background: var(--stage); position: relative; font-family: "Montserrat", sans-serif; }

  .cover { position: absolute; top: 90px; width: 400px; height: 620px; overflow: hidden; }

  /* Back cover */
  .back-cover { left: 185px; background: var(--back-bg); color: var(--back-teal); padding: 24px 26px; }
  .back-title { font-family: "Audiowide", sans-serif; font-weight: 400; font-size: 38px; line-height: 1.05; color: var(--back-teal); }
  .back-title .line { display: block; white-space: nowrap; }
  .back-title .tagline { font-size: 11px; color: var(--back-pink); vertical-align: top; margin-left: 6px; }
  .back-title .indent { padding-left: 40px; }
  .rule { height: 2px; background: var(--back-rule); margin: 14px -26px; }
  .back-heading { font-family: "Cinzel", serif; font-size: 17px; color: var(--back-head); margin: 6px 0 4px; }
  .back-body { font-family: "Cormorant Garamond", serif; font-style: italic; font-weight: 600; font-size: 14.5px; line-height: 1.3; text-indent: 70px; margin-bottom: 14px; }
  .back-extra { font-family: "Cinzel", serif; font-size: 13px; letter-spacing: 2px; color: var(--back-head); margin-top: 6px; }
  .back-info { font-family: "Cinzel", serif; font-size: 12px; letter-spacing: 2px; color: var(--back-muted); }
  .back-info small { display: block; font-size: 9px; margin-top: 6px; }

  /* Front cover */
  .front-cover { left: 615px; background: linear-gradient(180deg, var(--front-top) 0%, #fde2cf 30%, var(--front-mid) 70%, var(--front-warm) 100%); }
  .title-lead { position: absolute; left: 12px; top: 22px; font-family: "Montserrat", sans-serif; font-weight: 900; font-style: italic; font-size: 27px; line-height: 1.05; color: var(--title-yellow); -webkit-text-stroke: 1.2px var(--title-stroke); }
  .title-lead span { display: block; }
  .title-lead .second { padding-left: 18px; }
  .title-word { position: absolute; left: 122px; top: 26px; font-family: "Montserrat", sans-serif; font-weight: 900; font-size: 86px; line-height: 1; letter-spacing: 0; white-space: nowrap; }
  .h { color: var(--hope-h); } .o { color: var(--hope-o); } .p { color: var(--hope-p); } .e { color: var(--hope-e); }
  .subtitle { position: absolute; left: 6px; right: 6px; top: 124px; font-family: "Playfair Display", serif; font-style: italic; font-weight: 600; font-size: 12.5px; line-height: 1.3; text-align: center; color: var(--subtitle-blue); }
  .byline { position: absolute; right: 28px; top: 176px; font-family: "Playfair Display", serif; font-style: italic; font-weight: 600; font-size: 13px; line-height: 1.2; color: var(--byline); text-align: left; }

  .artwork { position: absolute; left: 0; top: 218px; width: 400px; height: 300px; }
  .theme-left, .theme-right { position: absolute; font-family: "Oswald", sans-serif; color: var(--word-yellow); line-height: 1; text-align: center; }
  .theme-left { left: 14px; top: 380px; }
  .theme-left .small { font-size: 19px; letter-spacing: 1px; display: block; }
  .theme-left .large { font-size: 46px; font-weight: 600; display: block; margin-top: 4px; }
  .theme-right { right: 10px; top: 330px; }
  .theme-right .small { font-size: 22px; display: block; }
  .theme-right .large { font-size: 32px; font-weight: 600; display: block; margin-top: 2px; }

  .band-message { position: absolute; left: 0; top: 518px; width: 100%; height: 24px; background: var(--band-orange); color: var(--white); font-family: "Montserrat", sans-serif; font-weight: 700; font-size: 10px; text-align: center; line-height: 24px; }
  .band-inspired { position: absolute; left: 0; top: 542px; width: 100%; height: 24px; background: var(--band-red); color: var(--title-yellow); font-family: "Montserrat", sans-serif; font-weight: 700; font-size: 12px; letter-spacing: 1px; text-align: center; line-height: 24px; }
  .band-author { position: absolute; left: 0; top: 566px; width: 100%; height: 54px; background: var(--band-black); color: var(--white); font-family: "Montserrat", sans-serif; font-weight: 700; font-size: 28px; letter-spacing: 1px; text-align: center; line-height: 54px; }
</style>
</head>
<body>

<section class="cover back-cover" aria-label="Back cover">
  <h2 class="back-title"><span class="line">AUTHOR<span class="tagline">- CARRY THE HOPE</span></span><span class="line indent">AUTHOR</span></h2>
  <div class="rule"></div>
  <h3 class="back-heading">About The Author</h3>
  <p class="back-body">This is a demo text only for representative purpose. For final copy the proper content should be edited consulting the author. This is a demo text only for representative purpose. For final copy the proper content should be edited consulting the author.</p>
  <h3 class="back-heading">About The Book</h3>
  <p class="back-body">This is a demo text only for representative purpose. For final copy the proper content should be edited consulting the author. This is a demo text only for representative purpose. For final copy the proper content should be edited consulting the author. This is a demo text only for representative purpose.</p>
  <div class="rule"></div>
  <p class="back-extra">ADDITIONAL INFO TEXT</p>
  <div class="rule"></div>
  <p class="back-info">INFO &amp; ADDRESS<small>WEBSITE ADDRESS</small></p>
</section>

<section class="cover front-cover" aria-label="Front cover">
  <svg class="artwork" viewBox="0 0 400 300" role="img" aria-label="Illustration: silhouette of a woman with outstretched arms rising above a city skyline, with butterflies and warm sunlight">
    <defs>
      <linearGradient id="art-glow" x1="0" y1="0" x2="0" y2="1">
        <stop offset="0" stop-color="#fcd9c4" stop-opacity="0"/>
        <stop offset="0.45" stop-color="#f9b86a"/>
        <stop offset="1" stop-color="#ef8a1f"/>
      </linearGradient>
    </defs>
    <rect width="400" height="300" fill="url(#art-glow)"/>
  </svg>

  <div class="title-lead"><span>CARRY</span><span class="second">THE</span></div>
  <h1 class="title-word"><span class="h">H</span><span class="o">O</span><span class="p">P</span><span class="e">E</span></h1>
  <p class="subtitle">shaped by <span class="h">H</span>eaven's <span class="o">O</span>utline to <span class="p">P</span>ursue <span class="e">E</span>xcellence in kindness to neighbours</p>
  <p class="byline">By<br>Author Name</p>

  <div class="theme-left"><span class="small">MANIFESTATION</span><span class="large">PURPOSE</span></div>
  <div class="theme-right"><span class="small">REWARD</span><span class="large">AUTHOR</span><span class="small">EMPOWERMENT</span></div>

  <div class="band-message">recognise the 'HOPE' of people feeling VALUED and LOVED</div>
  <div class="band-inspired">- Inspired From The Life Of My Daughter -</div>
  <div class="band-author">AUTHOR NAME</div>
</section>

</body>
</html>
```